Flyer für selbstständigen Finanzierungsvermittler  für Baufinanzierungen
Flyer für selbstständigen Finanzierungsvermittler für Baufinanzierungen
Zielgruppe
seit 1999 selbstständiger Finanzierungsvermittler für Baufinanzierungen.
ich arbeite für (nicht angestellt) ein Maklerbüro in Schorndorf, hier wurde vor Jahren ein Flyer konzepiert.
Zukünftiger Flyer soll von Immobilienmaklern Interessenten ausgehändigt oder in Kundenmappe KEV-Maklerbüro beigelegt werden.
Aufgabenstellung
- der beigefügte Flyer von Dieter Wallbrunn hat schon sehr viel von dem, was ich mir das vorstelle
- die Farben des Maklerbüros sind Blau und weiß, kann aber auch ganz anders entworfen werden
- Es soll ein DinA 4 Flyer werden, ebenso die PDF-Datei hierzu
- Adressfeld: Gregor Sandberg, Baufinanzierungsspezialist, Bankkaufmann, Kesselweg 14, 73541 Feldheim, Mobil 0152 647 3185, gregor@sandbrg58.de
Text für den Flyer, anlehnend an beileigende:
- Längjährige Erfahrung
- Vergleich von über 300 Banken
- Top Konditionen, bis zu 40 Jahre Zinsbindung
- Beratung vor Ort, auch per Viseo und Telefon möglich
- rasche Zusage, aufgrund persönlichem Kontakt zu Entscheidungsträgern der Bank
mitgelieferte Bilder dürfen natürlich zugeschnitten werden (nur bis Brust) oder weniger Hintergrund, etc.

```html
<!DOCTYPE html>
<html lang="de">
<head>
<meta charset="utf-8">
<title>Flyer Gregor Sandberg – Baufinanzierung</title>
<link rel="stylesheet" href="https://fonts.googleapis.com/css2?family=Open+Sans:wght@400;600;700&family=Raleway:wght@400;500&display=swap">
<style>
  :root {
    --brand-blue: #0068b4;
    --navy: #003f6f;
    --charcoal: #33363b;
    --photo-light: #dfe9f3;
    --photo-mid: #aebccb;
    --light-blue-text: #93c7ee;
    --ink: #1c1c1c;
    --white: #ffffff;
    --stage-top: #ebebeb;
    --stage-bottom: #d6d6d6;
  }
  * { margin: 0; padding: 0; box-sizing: border-box; }
  html, body { width: 1200px; height: 2382px; overflow: hidden; }
  body {
    position: relative;
    background: var(--white);
    font-family: "Open Sans", Arial, sans-serif;
  }
  .stage-lower {
    position: absolute; left: 0; top: 1355px; width: 1200px; height: 1027px;
    background: linear-gradient(var(--stage-top), var(--stage-bottom));
  }
  .flyer {
    position: absolute; left: 233px; top: 133px; width: 867px; height: 1224px;
    background: var(--white);
    box-shadow: 0 8px 40px rgba(0,0,0,0.28);
    overflow: hidden;
  }
  .flyer-shapes { position: absolute; inset: 0; }
  .tagline {
    position: absolute; left: 520px; top: 60px;
    display: flex; align-items: center; gap: 18px;
    color: var(--white); font-size: 11.5px; font-weight: 600; letter-spacing: 1.6px;
  }
  .tagline-dot {
    width: 26px; height: 26px; border: 2px solid var(--white); border-radius: 50%;
  }
  .name {
    position: absolute; left: 78px; top: 180px;
    color: var(--brand-blue); font-size: 66px; font-weight: 400; line-height: 62px;
    letter-spacing: 0.5px;
  }
  .contact {
    position: absolute; left: 84px; top: 394px;
    color: var(--ink); font-size: 12px; line-height: 16.5px;
  }
  .contact-heading { color: var(--brand-blue); font-weight: 700; font-size: 11px; margin-bottom: 14px; }
  .contact-role { margin-bottom: 16px; }
  .benefit {
    position: absolute; transform: translateX(-50%);
    text-align: center; white-space: nowrap;
    font-family: "Raleway", "Open Sans", sans-serif;
  }
  .benefit-main { top: 770px; color: var(--white); font-size: 20px; font-weight: 500; line-height: 29px; letter-spacing: 0.4px; }
  .benefit-main svg { display: block; margin: 0 auto 12px; }
  .benefit-sub { top: 963px; color: var(--light-blue-text); font-size: 16px; font-weight: 500; line-height: 22px; letter-spacing: 0.3px; }
  .benefit-sub svg { display: block; margin: 0 auto 10px; }
</style>
</head>
<body>
  <div class="stage-lower"></div>

  <article class="flyer">
    <svg class="flyer-shapes" width="867" height="1224" viewBox="0 0 867 1224">
      <defs>
        <linearGradient id="portraitTone" x1="0" y1="0" x2="1" y2="1">
          <stop offset="0" stop-color="var(--photo-light)"/>
          <stop offset="0.6" stop-color="var(--photo-mid)"/>
          <stop offset="1" stop-color="#3a3f48"/>
        </linearGradient>
      </defs>
      <polygon class="header-band" points="312,0 867,0 867,115 499,152" fill="var(--charcoal)"/>
      <polygon class="portrait" role="img" aria-label="Porträtfoto des Baufinanzierungsberaters im Anzug vor hellem Büro" points="499,152 867,115 867,667 387,570" fill="url(#portraitTone)"/>
      <polygon class="accent-strip" points="387,570 867,667 867,689 327,604" fill="var(--brand-blue)"/>
      <polygon class="benefit-panel" points="0,777 327,604 867,689 747,1224 0,1224" fill="var(--navy)"/>
      <polygon class="accent-edge" points="867,689 867,1224 747,1224" fill="var(--brand-blue)"/>
      <g stroke="var(--brand-blue)" stroke-width="1.5" fill="none">
        <line x1="122" y1="0" x2="499" y2="152"/>
        <line x1="499" y1="152" x2="387" y2="570"/>
        <line x1="0" y1="687" x2="327" y2="604"/>
        <polyline points="0,1224 247,1139 747,1224"/>
      </g>
    </svg>

    <div class="tagline"><span class="tagline-dot"></span>IHR BAUFINANZIERUNGSSPEZIALIST</div>

    <h1 class="name">GREGOR<br>SANDBERG</h1>

    <div class="contact">
      <p class="contact-heading">KONTAKT</p>
      <p class="contact-role">Gregor Sandberg&nbsp; | &nbsp;Bankkaufmann</p>
      <p>Kesselweg 14 |&nbsp; 73541 Feldheim</p>
      <p>Mobil 0152 647 3185</p>
      <p>gregor@sandbrg58.de</p>
    </div>

    <div class="benefit benefit-main" style="left:192px">
      <svg width="46" height="30" viewBox="0 0 46 30"><path d="M3 15 L16 27 Q26 8 44 2" stroke="var(--white)" stroke-width="5" fill="none" stroke-linecap="round" stroke-linejoin="round"/></svg>
      LÄNGJÄHRIGE<br>ERFAHRUNG
    </div>
    <div class="benefit benefit-main" style="left:392px">
      <svg width="46" height="30" viewBox="0 0 46 30"><path d="M3 15 L16 27 Q26 8 44 2" stroke="var(--white)" stroke-width="5" fill="none" stroke-linecap="round" stroke-linejoin="round"/></svg>
      VERGLEICH<br>VON ÜBER<br>300 BANKEN
    </div>
    <div class="benefit benefit-main" style="left:622px">
      <svg width="46" height="30" viewBox="0 0 46 30"><path d="M3 15 L16 27 Q26 8 44 2" stroke="var(--white)" stroke-width="5" fill="none" stroke-linecap="round" stroke-linejoin="round"/></svg>
      TOP KONDITIONEN<br>BIS ZU 40 JAHRE<br>ZINSBINDUNG
    </div>

    <div class="benefit benefit-sub" style="left:222px">
      <svg width="38" height="36" viewBox="0 0 38 36" fill="none" stroke="var(--light-blue-text)" stroke-width="1.6"><path d="M19 2 C29 2 36 8 36 16 C36 24 29 30 19 30 C16 30 13 29 11 28 L3 33 L6 25 C3 22 2 19 2 16 C2 8 9 2 19 2 Z"/><line x1="11" y1="11" x2="27" y2="11"/><line x1="11" y1="15" x2="27" y2="15"/><line x1="11" y1="19" x2="27" y2="19"/><line x1="11" y1="23" x2="24" y2="23"/></svg>
      BERATUNG VOR ORT<br>AUCH PER VIDEO UND<br>TELEFON MÖGLICH
    </div>
    <div class="benefit benefit-sub" style="left:539px">
      <svg width="44" height="36" viewBox="0 0 44 36" fill="none" stroke="var(--light-blue-text)" stroke-width="1.6"><rect x="3" y="5" width="24" height="29" rx="2"/><rect x="10" y="2" width="10" height="6" rx="1"/><line x1="8" y1="14" x2="22" y2="14"/><line x1="8" y1="19" x2="22" y2="19"/><line x1="8" y1="24" x2="18" y2="24"/><path d="M24 26 L38 6 L42 9 L28 29 L23 31 Z"/></svg>
      RASCHE ZUSAGE, AUFGRUND<br>PERSÖNLICHEM KONTAKT ZU<br>ENTSCHEIDUNGSTRÄGERN DER BANK
    </div>
  </article>
</body>
</html>
```